Homes, Invest in Non-performing loans

We need only 3 web pages, one for the home, one for the content, one for the properties.
The main focus of our business is to offer non performing loans (before foreclosures) to the general public. All the non-performing mortgages will end in a house, an apartment, a store, etc.
Our customers are able to invest from 10,000usd to 1,000,000usd (average 50,000usd).
Our customers' usual focus groups are employees who want second earnings, perceiving the business feeling without outlay time. They look for a solid finance sense corporation that confers them certainty.
Nearly all our clients desire the house, apartment, store, etc. more than the actual earnings.
The name of our company is BRAMLEY
Reason: We value the time and effort you already invest in our project. We realize that we did't come back on some of the doubts requested by the designers. It will be inequitable to the designers who prerequisite our feedback. We also appreciate the comprehension of the community in this postponement.
Reason: Designers,
We really apreciate all the time and effort you put on our project. From the begining we ask for 3 pages, so now we will leave the 10 finalist and provide some extra time to submit the other 2 pages.
We will race the price in 10%
Target Market(s)
Our customers average investors works as employees and want to have a second income or business without spending time. (People from 35 to 50)
Industry/Entity Type
Finance
Requirements
Should not have
- FLASH

```html
<!DOCTYPE html>
<html lang="en">
<head>
<meta charset="utf-8">
<title>Bramley – Remates Hipotecarios</title>
<link rel="stylesheet" href="https://fonts.googleapis.com/css2?family=PT+Sans:wght@400;700&family=Open+Sans:wght@400;600&display=swap">
<style>
:root{
  --blue-deep:#2659a6;
  --blue-mid:#3a69ae;
  --blue-pale:#8199c6;
  --navy:#123f8f;
  --olive:#b1a833;
  --olive-dark:#8f8825;
  --white:#ffffff;
  --ink:#2b2b2b;
  --footer:#b2a836;
}
*{margin:0;padding:0;box-sizing:border-box}
html,body{width:1200px;height:1046px;overflow:hidden}
body{position:relative;font-family:"Open Sans",sans-serif;color:var(--ink);
  background:var(--blue-pale)}
.hero{position:absolute;left:0;top:0;width:1200px;height:480px;
  background:linear-gradient(180deg,var(--blue-deep) 0%,var(--blue-mid) 62%,#5f80b8 85%,var(--blue-pale) 100%)}
.hero-photo{position:absolute;left:0;top:220px;width:1200px;height:260px;
  background:linear-gradient(165deg,rgba(255,255,255,0) 30%,rgba(210,215,225,.25) 55%,rgba(129,153,198,0) 90%)}
.brand-ribbon{position:absolute;left:318px;top:0;width:96px;height:143px}
.brand-name{position:absolute;left:318px;top:34px;width:96px;text-align:center;
  font-family:"PT Sans",sans-serif;font-weight:700;font-size:21px;color:#333;letter-spacing:.5px}
.brand-dot{position:absolute;left:360px;top:12px;width:14px;height:14px;background:var(--olive)}
.brand-tag{position:absolute;left:318px;top:74px;width:96px;text-align:center;
  font-size:5.5px;letter-spacing:.6px;color:#444}
.account{position:absolute;top:14px;left:760px;font-size:7px;color:var(--white);display:flex;gap:10px}
.social{position:absolute;display:flex;gap:3px}
.social span{width:14px;height:14px;border-radius:3px;background:#d8e3ef}
.social-top{left:815px;top:12px}
.main-nav{position:absolute;left:498px;top:58px;width:384px;height:34px;background:var(--olive);
  box-shadow:0 3px 4px rgba(0,0,0,.35);display:flex;align-items:center}
.main-nav a{flex:1;text-align:center;color:var(--white);font-family:"PT Sans",sans-serif;
  font-weight:700;font-size:10px;text-decoration:none}
.hero-title{position:absolute;top:150px;width:1200px;text-align:center;color:var(--white);
  font-family:"PT Sans",sans-serif;font-weight:700;font-size:31px}
.hero-sub{position:absolute;top:190px;width:1200px;text-align:center;color:var(--white);
  font-family:"PT Sans",sans-serif;font-weight:700;font-size:13px}
.hero-art{position:absolute;left:424px;top:242px;width:372px;height:166px;border-radius:6px;
  background:radial-gradient(ellipse at 45% 55%,rgba(220,228,240,.75),rgba(60,100,170,.35) 70%,rgba(60,100,170,0))}
.hero-arrow{position:absolute;top:238px}
.dots{position:absolute;top:425px;left:582px;display:flex;gap:3px}
.dots span{width:11px;height:11px;border-radius:50%;background:var(--white)}
.dots span.active{background:var(--olive)}
.panel{position:absolute;background:var(--white);box-shadow:0 0 0 3px rgba(90,115,170,.5)}
.panel h2{font-family:"PT Sans",sans-serif;font-weight:700;font-size:16px;color:var(--navy)}
.how{left:318px;top:488px;width:276px;height:249px}
.how h2{position:absolute;left:25px;top:18px}
.how p{position:absolute;left:25px;top:52px;width:232px;font-size:9.6px;line-height:10.9px}
.news{left:606px;top:488px;width:276px;height:249px}
.news h2{position:absolute;left:24px;top:18px}
.news-item{position:absolute;left:24px;display:flex;gap:6px;width:232px}
.news-thumb{width:36px;height:34px;flex:none;background:linear-gradient(90deg,#6b7f88 0 25%,#a6d12a 25%);box-shadow:1px 1px 2px rgba(0,0,0,.3)}
.news-item p{font-size:8.3px;line-height:10.6px}
.btn{position:absolute;width:72px;height:24px;background:var(--olive);color:var(--white);
  font-size:7.5px;display:flex;align-items:center;justify-content:center;
  box-shadow:1px 2px 2px rgba(0,0,0,.35);border-bottom:2px solid var(--olive-dark)}
.services{left:318px;top:775px;width:564px;height:104px}
.services h2{position:absolute;left:24px;top:10px}
.service{position:absolute;top:37px;width:70px;text-align:center;font-size:7.5px;color:var(--navy)}
.service svg,.service .figure{display:block;margin:0 auto 5px;width:38px;height:38px}
.figure{background:var(--navy);border-radius:6px}
.services-next{position:absolute;left:528px;top:30px}
.site-footer{position:absolute;left:0;top:914px;width:1200px;height:132px;background:var(--footer)}
.footer-nav{position:absolute;left:318px;top:24px;display:flex;gap:8px;font-size:7.5px;color:var(--white)}
.follow{position:absolute;left:808px;top:23px;font-size:7.5px;color:var(--white)}
.social-foot{left:808px;top:39px}
.social-foot span{width:16px;height:16px}
.copyright{position:absolute;left:318px;top:67px;font-size:6.5px;color:var(--white)}
.copyright b{font-size:7.5px}
</style>
</head>
<body>
<header class="hero">
  <div class="hero-photo" role="img" aria-label="Photo of a white house roof edge against a blue sky"></div>
  <svg class="brand-ribbon" viewBox="0 0 96 143"><polygon points="0,0 96,0 96,143 48,95 0,143" fill="#fff"/></svg>
  <span class="brand-dot"></span>
  <div class="brand-name">BRAMLEY</div>
  <div class="brand-tag">REMATES HIPOTECARIOS</div>
  <div class="account"><span>Login</span><span>Signup</span></div>
  <div class="social social-top"><span></span><span></span><span></span><span></span></div>
  <nav class="main-nav"><a href="#">Home</a><a href="#">About</a><a href="#">Services</a><a href="#">Contact</a></nav>
  <h1 class="hero-title">Jujubes jelly beans</h1>
  <p class="hero-sub">Pastry cake biscuit jujubes oat cake. Candy canes candy canes topping lemon</p>
  <div class="hero-art" role="img" aria-label="Illustration of a house with a key and banknotes"></div>
  <svg class="hero-arrow" style="left:272px" width="22" height="30" viewBox="0 0 22 30"><polyline points="18,3 6,15 18,27" fill="none" stroke="#b9c2cf" stroke-width="6"/></svg>
  <svg class="hero-arrow" style="left:908px" width="22" height="30" viewBox="0 0 22 30"><polyline points="4,3 16,15 4,27" fill="none" stroke="#b9c2cf" stroke-width="6"/></svg>
  <div class="dots"><span class="active"></span><span></span><span></span></div>
</header>

<section class="panel how">
  <h2>How we work</h2>
  <p>Jujubes jelly beans pastry cake biscuit jujubes oat cake. Candy canes candy canes topping lemon drops liquorice. Faworki chocolate bar cookie tart powder tootsie roll macaroon liquorice.<br>Bonbon fruitcake croissant. Danish sugar plum danish croissant topping wafer. Candy lollipop lemon drops tart lollipop bear claw tootsie roll wypas fruitcake.<br>Bonbon fruitcake croissant. Danish sugar plum danish croissant topping wafer. Candy lollipop lemon drops tart lollipop bear claw tootsie roll wypas fruitcake.Bonbon fruitcake croissant. Danish sugar plum danish croissant topping wafer. Candy lollipop</p>
  <a class="btn" style="left:180px;top:208px">see our offers</a>
</section>

<section class="panel news">
  <h2>News</h2>
  <div class="news-item" style="top:52px"><div class="news-thumb" role="img" aria-label="Photo of a green front door"></div><p>Jujubes jelly beans pastry cake biscuit jujubes oat cake. Candy canes candy canes topping lemon drops liquorice.</p></div>
  <div class="news-item" style="top:104px"><div class="news-thumb" role="img" aria-label="Photo of a green front door"></div><p>Jujubes jelly beans pastry cake biscuit jujubes oat cake. Candy canes candy canes topping lemon drops liquorice.</p></div>
  <div class="news-item" style="top:157px"><div class="news-thumb" role="img" aria-label="Photo of a green front door"></div><p>Jujubes jelly beans pastry cake biscuit jujubes oat cake. Candy canes candy canes topping lemon drops liquorice.</p></div>
  <a class="btn" style="left:180px;top:208px">more news</a>
</section>

<section class="panel services">
  <h2>Our Services</h2>
  <div class="service" style="left:11px"><div class="figure" role="img" aria-label="Icon of a family"></div>Lorem ipsum</div>
  <div class="service" style="left:93px"><svg viewBox="0 0 38 38"><g fill="#123f8f"><circle cx="19" cy="19" r="12"/><g stroke="#123f8f" stroke-width="6"><line x1="19" y1="3" x2="19" y2="35"/><line x1="3" y1="19" x2="35" y2="19"/><line x1="8" y1="8" x2="30" y2="30"/><line x1="30" y1="8" x2="8" y2="30"/></g></g><circle cx="19" cy="19" r="5" fill="#fff"/></svg>Lorem ipsum</div>
  <div class="service" style="left:174px"><svg viewBox="0 0 38 38"><polygon points="14,2 24,2 22,26 16,26" fill="#123f8f"/><rect x="15" y="29" width="8" height="7" fill="#123f8f"/></svg>Lorem ipsum</div>
  <div class="service" style="left:258px"><div class="figure" role="img" aria-label="Icon of a strategy board"></div>Lorem ipsum</div>
  <div class="service" style="left:353px"><svg viewBox="0 0 38 38"><path d="M3 16 L9 6 H29 L35 16 V32 H3 Z" fill="#123f8f"/><rect x="8" y="10" width="22" height="2" fill="#fff"/><path d="M3 16 H13 V20 H25 V16 H35" fill="none" stroke="#fff" stroke-width="2"/></svg>Lorem ipsum</div>
  <div class="service" style="left:437px"><svg viewBox="0 0 38 38"><polygon points="19,3 36,18 31,18 31,35 7,35 7,18 2,18" fill="#123f8f"/><rect x="26" y="5" width="4" height="8" fill="#123f8f"/><rect x="15" y="20" width="8" height="8" fill="#fff"/></svg>Lorem ipsum</div>
  <svg class="services-next" width="14" height="44" viewBox="0 0 14 44"><polyline points="3,2 11,22 3,42" fill="none" stroke="#b9c6dd" stroke-width="4"/></svg>
</section>

<footer class="site-footer">
  <nav class="footer-nav"><span>Home</span><span>About</span><span>Services</span><span>Contact</span></nav>
  <div class="follow">Follow us on</div>
  <div class="social social-foot"><span></span><span></span><span></span><span></span></div>
  <p class="copyright"><b>Bramley.</b> All rights reserved Copyright 2013</p>
</footer>
</body>
</html>
```